Design required for boutique fire engineering firm in New Zealand

Our website was published based on free Wordpress templates, we'd like something a bit more bespoke, clean and simple.

Reason: didn't check this finished on a Sunday :)

Target Market(s)

architects, building owners, property developers

Industry/Entity Type

Boutique

Contact Information for Business Card

Logo
Fire Engineering

Derek Holloway
Principal
+64 21 738 152
derek@veltraxa.nz
veltraxa.nz

Number of Pages Required

3 page

Font styles to use
Sans Serif

Requirements
Nice to have
• On the business card, an embossed logo would be great - not sure if that's a design thing or just a print thing?
• Website, existing @ http://veltraxa.nz for extent of content and general arrangement that I'm happy with.
• Ability to update the content with project bio's and some photos at a later date would be nice.

```html
<!DOCTYPE html>
<html lang="en">
<head>
<meta charset="utf-8">
<title>Veltraxa Business Card</title>
<link rel="stylesheet" href="https://fonts.googleapis.com/css2?family=Oswald:wght@400;500;600&display=swap">
<style>
  :root {
    --backdrop: #c9c9c9;
    --paper: #ffffff;
    --navy: #054f7e;
    --navy-deep: #0a4a78;
    --blue: #3574b5;
    --ghost: #f1f2f5;
    --ink-light: #ffffff;
    --icon-soft: #a9c3da;
  }
  * { margin: 0; padding: 0; box-sizing: border-box; }
  html, body { width: 1200px; height: 1200px; overflow: hidden; }
  body {
    background: var(--backdrop);
    font-family: "Oswald", sans-serif;
    position: relative;
  }
  .card {
    position: absolute;
    left: 150px;
    width: 900px;
    height: 514px;
    overflow: hidden;
  }
  .card-front { top: 56px; background: var(--paper); }
  .card-back { top: 630px; background: var(--navy); color: var(--ink-light); }

  .stripes { position: absolute; left: 0; top: 0; }

  .ghost-disc {
    position: absolute;
    right: 40px; top: 60px;
    width: 400px; height: 400px;
    border-radius: 50%;
    border: 46px solid var(--ghost);
  }
  .brand {
    position: absolute;
    left: 330px; top: 212px;
    display: flex; align-items: center; gap: 18px;
  }
  .brand-dot {
    width: 62px; height: 62px; border-radius: 50%;
    background: var(--navy-deep);
  }
  .brand-name {
    font-size: 72px; font-weight: 500; line-height: 1;
    color: var(--navy-deep); letter-spacing: 1px;
  }

  .emboss-disc {
    position: absolute;
    left: 120px; top: 110px;
    width: 340px; height: 340px;
    border-radius: 50%;
    border: 30px solid rgba(53, 116, 181, 0.55);
  }
  .identity {
    position: absolute;
    right: 110px; top: 70px;
    text-align: right;
  }
  .person-name { font-size: 50px; font-weight: 600; line-height: 1.05; letter-spacing: 0.5px; }
  .person-title { font-size: 18px; font-weight: 400; letter-spacing: 3px; margin-top: 4px; }
  .contacts {
    position: absolute;
    right: 60px; top: 210px;
    list-style: none;
  }
  .contacts li {
    display: flex; justify-content: flex-end; align-items: center;
    gap: 22px; margin-bottom: 20px;
    font-size: 19px; text-align: right; line-height: 1.2;
  }
  .contacts svg { width: 16px; height: 16px; flex: none; }
</style>
</head>
<body>

<section class="card card-front" aria-label="Card front">
  <svg class="stripes" width="900" height="514" viewBox="0 0 900 514" aria-hidden="true">
    <polygon points="150,0 232,0 162,514 80,514" fill="var(--navy-deep)"/>
    <polygon points="262,0 344,0 274,514 192,514" fill="var(--blue)"/>
  </svg>
  <div class="ghost-disc" aria-hidden="true"></div>
  <div class="brand">
    <span class="brand-dot" aria-hidden="true"></span>
    <span class="brand-name">veltraxa</span>
  </div>
</section>

<section class="card card-back" aria-label="Card back">
  <div class="emboss-disc" aria-hidden="true"></div>
  <div class="identity">
    <h1 class="person-name">Derek Holloway</h1>
    <p class="person-title">Principal, Fire Engineer</p>
  </div>
  <ul class="contacts">
    <li>Lorem Ipsum is simplydummy text of the printing
      <svg viewBox="0 0 16 16" aria-hidden="true"><path d="M8 1a5 5 0 0 1 5 5c0 4-5 9-5 9S3 10 3 6a5 5 0 0 1 5-5z" fill="none" stroke="var(--icon-soft)" stroke-width="1.4"/><circle cx="8" cy="6" r="1.8" fill="var(--icon-soft)"/></svg>
    </li>
    <li>021 738 152
      <svg viewBox="0 0 16 16" aria-hidden="true"><path d="M4 2l3 3-2 2a8 8 0 0 0 4 4l2-2 3 3-2 2C7 14 2 9 2 4z" fill="none" stroke="var(--icon-soft)" stroke-width="1.4" stroke-linejoin="round"/></svg>
    </li>
    <li>info@veltraxa.com
      <svg viewBox="0 0 16 16" aria-hidden="true"><rect x="1.5" y="3.5" width="13" height="9" fill="none" stroke="var(--icon-soft)" stroke-width="1.4"/><path d="M1.5 3.5 8 9l6.5-5.5" fill="none" stroke="var(--icon-soft)" stroke-width="1.4"/></svg>
    </li>
    <li>www.veltraxa.nz
      <svg viewBox="0 0 16 16" aria-hidden="true"><circle cx="8" cy="8" r="6.5" fill="none" stroke="var(--icon-soft)" stroke-width="1.4"/><ellipse cx="8" cy="8" rx="2.8" ry="6.5" fill="none" stroke="var(--icon-soft)" stroke-width="1.2"/><path d="M1.5 8h13" stroke="var(--icon-soft)" stroke-width="1.2"/></svg>
    </li>
  </ul>
</section>

</body>
</html>
```